Brochure design for a Driftly Video Booth!

We are after a brochure for a Driftly Video Booth product being launched very soon. Attached are the logo, photos and all required information to be included in this brochure.

I have also attached a number of "inspiration" designs to show you the style we are after.

The colours should be black, white and a warm yellow (see attachment).

The brochure is for online use only, so does not need to constrain to typical printing specs. A square or rectangular booklet would be preferable.

Target Market(s)

Couples getting married between 20 - 35.

Industry/Entity Type

Printing

Font styles to use
Serif
Sans Serif

Colors
fece3e
000000
ffffff

Requirements
Must have
• at least 4 pages, a 'typography' design feel, good use of space. The colours should be black, white and a warm yellow (see attachment). Feel free to use whatever layout you think would work best.
Should not have
• Clutter.

```html
<!DOCTYPE html>
<html lang="en">
<head>
<meta charset="utf-8">
<title>Driftly Video Booth – Extras</title>
<link rel="stylesheet" href="https://fonts.googleapis.com/css2?family=League+Gothic&family=Oswald:wght@200;500&family=Varela+Round&family=Roboto:wght@700&display=swap">
<style>
  :root {
    --yellow: #fec20e;
    --black: #000000;
    --white: #ffffff;
  }
  * { margin: 0; padding: 0; box-sizing: border-box; }
  html, body { width: 927px; height: 1200px; overflow: hidden; background: var(--white); }
  .page {
    position: relative;
    width: 927px;
    height: 1200px;
    overflow: hidden;
    background: var(--white);
  }
  .wordmark-wall {
    position: absolute;
    left: 0; top: 0;
    width: 927px; height: 565px;
    overflow: hidden;
  }
  .wall-row {
    position: absolute;
    left: 0; width: 927px;
    display: flex;
    justify-content: center;
    white-space: nowrap;
    font-family: "League Gothic", "Oswald", sans-serif;
    font-size: 345px;
    line-height: 1;
    color: var(--black);
    overflow: hidden;
  }
  .wall-row--top { top: -128px; }
  .wall-row--middle { top: 148px; }
  .wall-row--bottom { top: 428px; }
  .wall-row .highlight { color: var(--yellow); }

  .extras-panel {
    position: absolute;
    left: 0; top: 565px;
    width: 927px; height: 611px;
    background: var(--black);
  }
  .extras-title {
    position: absolute;
    left: 0; right: 0; top: 30px;
    text-align: center;
    font-family: "Oswald", sans-serif;
    font-weight: 200;
    font-size: 80px;
    letter-spacing: 0.55em;
    padding-left: 0.55em;
    line-height: 1;
    color: var(--yellow);
  }
  .extra {
    position: absolute;
    font-family: "Varela Round", sans-serif;
    font-size: 16.5px;
    line-height: 26px;
    text-align: justify;
    text-align-last: right;
  }
  .extra h2 {
    font-family: "Oswald", sans-serif;
    font-weight: 500;
    font-size: 21px;
    line-height: 26px;
    text-transform: uppercase;
    text-align: left;
    text-align-last: left;
  }
  .extra--time { left: 28px; top: 186px; width: 521px; color: var(--yellow); }
  .extra--bottles { left: 337px; top: 392px; width: 552px; color: var(--white); }

  .site-band {
    position: absolute;
    left: 0; top: 1176px;
    width: 927px; height: 24px;
    background: var(--yellow);
    text-align: center;
    font-family: "Roboto", sans-serif;
    font-weight: 700;
    font-size: 20px;
    line-height: 24px;
    color: var(--black);
  }
</style>
</head>
<body>
  <main class="page">
    <div class="wordmark-wall" aria-hidden="true">
      <div class="wall-row wall-row--top">Driftly Driftly Driftly</div>
      <div class="wall-row wall-row--middle">ftly&nbsp;<span class="highlight">Driftly</span>&nbsp;Dr</div>
      <div class="wall-row wall-row--bottom">tly Driftly Dri</div>
    </div>

    <section class="extras-panel">
      <h1 class="extras-title">Extras</h1>

      <article class="extra extra--time">
        <h2>Additional time: $300 per hour</h2>
        <p>This includes the extra props and personal to get through each additional hour. For weddings 2 hours is the perfect time, however if you are booking the Driftly Booth for an event you may need more time depending on your events schedule.</p>
      </article>

      <article class="extra extra--bottles">
        <h2>SFX glass bottles: $150</h2>
        <p>This includes 4 special effects breakaway wine or beer bottles that you can smash across someone’s head, it doesn’t get any better then this! These bottles have been specially made to shatter on impact and they do not hurt. They are from an Australian special effects company.</p>
      </article>
    </section>

    <footer class="site-band">www.driftly.com.au</footer>
  </main>
</body>
</html>
```